Trade Show Booth

We need a Single booth design size and below are the requirements from the event holder.
How to provide graphics:
Single booth: Graphic size is 1993 mm width x 2483 mm height
Naming file: Name the files as Company name_ size_scale_bleed, for example: “Roam Kestal_1993x2483mm_scale1_10_ bleed50mm.”
Bleed & Marks: 50mm bleed all around, no marks, and no crop marks.
Resolution: Please try to keep graphics over 100 dpi to maintain good quality.

We are a DMC in Iceland and will be participating in a Travel show.
www.brightfjordtrips.example

We would like to work with someone who could help us create this and potentially some marketing material for the show.

```html
<!DOCTYPE html>
<html lang="en">
<head>
<meta charset="utf-8">
<title>Roam Kestal – Trade Show Booth</title>
<link href="https://fonts.googleapis.com/css2?family=Poppins:wght@500;700;800;900&family=Kaushan+Script&display=swap" rel="stylesheet">
<style>
  :root{
    --stage:#dcdde2;
    --navy:#0d2344;
    --aurora:#1f8f7a;
    --glacier:#2a5aa8;
    --deep:#14264f;
    --sky:#1a9fe0;
    --url:#23b5ec;
    --yellow:#f5e600;
    --lime:#d6f000;
    --mint:#35e0b4;
    --orange:#f39200;
    --red:#d41f3c;
    --royal:#2f5ee0;
    --white:#ffffff;
  }
  *{margin:0;padding:0;box-sizing:border-box}
  html,body{width:750px;height:1200px;overflow:hidden;background:var(--stage)}
  body{font-family:"Poppins",sans-serif;position:relative}
  .booth-graphic{position:absolute;left:0;top:133px;width:750px;height:934px;overflow:hidden;background:var(--white)}
  .scene-top{position:absolute;left:0;top:0;width:750px;height:420px;
    background:linear-gradient(180deg,#1a6f6a 0%,var(--aurora) 10%,#2c5f9c 35%,var(--glacier) 60%,#2f6cc0 100%)}
  .scene-bottom{position:absolute;left:0;top:600px;width:750px;height:334px;
    background:linear-gradient(180deg,rgba(255,255,255,0) 0%,#9aa6bb 18%,#5b6a86 45%,#2a3450 75%,#141a2c 100%)}
  .torn-panel{position:absolute;left:0;top:395px;width:750px;height:260px}
  .join{position:absolute;left:318px;top:26px;font-family:"Kaushan Script",cursive;font-size:56px;color:var(--navy);z-index:2}
  .headline{position:absolute;left:0;width:750px;top:52px;text-align:center;font-weight:800;font-size:100px;letter-spacing:-3px;color:var(--white);line-height:1}
  .biggest-band{position:absolute;left:294px;top:143px;width:152px;height:32px;background:var(--mint);transform:skewX(-8deg);border-radius:3px}
  .biggest{position:absolute;left:294px;top:143px;width:152px;text-align:center;font-weight:800;font-size:25px;color:var(--navy);line-height:32px}
  .tours{position:absolute;left:0;width:750px;top:172px;text-align:center;font-family:"Kaushan Script",cursive;font-size:62px;color:var(--yellow);line-height:1.1}
  .exhibition{position:absolute;left:0;width:750px;top:240px;text-align:center;font-weight:500;font-size:22px;letter-spacing:10px;color:var(--white)}
  .info-box{position:absolute;left:89px;top:294px;width:570px;height:110px;border-radius:10px 10px 0 0;
    background:linear-gradient(90deg,#1a8fe0,var(--sky) 60%,#27b0f0)}
  .booth-no{position:absolute;left:47px;top:19px;width:84px;height:53px;background:var(--navy);border-radius:7px;text-align:center;color:var(--white)}
  .booth-no small{display:block;font-size:10px;font-weight:700;color:var(--mint);padding-top:3px;line-height:1}
  .booth-no strong{display:block;font-size:35px;font-weight:800;line-height:38px}
  .info-text{position:absolute;left:147px;top:18px;width:400px;font-size:14px;font-weight:500;line-height:18px;color:var(--white)}
  .tag{position:absolute;height:25px;padding-left:11px;font-weight:800;font-size:20px;line-height:25px;border-radius:4px 0 0 4px;white-space:nowrap}
  .tag.tall{height:60px;font-size:19px;line-height:19px;padding-top:2px}
  .tag-caves{left:62px;top:442px;width:150px;background:linear-gradient(90deg,var(--lime),rgba(214,240,0,0.1));color:var(--navy)}
  .tag-atv{left:62px;top:514px;width:150px;background:linear-gradient(90deg,var(--orange),rgba(243,146,0,0.05));color:var(--navy)}
  .tag-boat{left:62px;top:551px;width:150px;background:linear-gradient(90deg,#33a6e0,rgba(51,166,224,0.05));color:var(--white)}
  .tag-sightseeing{left:222px;top:444px;width:230px;background:linear-gradient(90deg,var(--royal),rgba(47,94,224,0.05));color:var(--white)}
  .tag-glacier{left:222px;top:480px;width:230px;background:linear-gradient(90deg,#2fe0b0,rgba(47,224,176,0.05));color:var(--navy)}
  .tag-whale{left:222px;top:516px;width:230px;background:linear-gradient(90deg,#e0304a,rgba(224,48,74,0.05));color:var(--navy)}
  .tag-buggy{left:222px;top:551px;width:230px;background:linear-gradient(90deg,var(--deep),rgba(20,38,79,0.05));color:var(--white)}
  .tag-jeep{left:222px;top:587px;width:200px;background:linear-gradient(90deg,var(--yellow),rgba(245,230,0,0.05));color:var(--navy)}
  .snapshot{position:absolute;background:var(--white);padding:6px;box-shadow:0 4px 10px rgba(0,0,0,0.25)}
  .snapshot div{width:100%;height:100%}
  .snap-cave{left:470px;top:382px;width:184px;height:126px;transform:rotate(-3deg)}
  .snap-cave div{background:linear-gradient(135deg,#8a6a3e,#5a3f22 60%,#2a1d12)}
  .snap-jeeps{left:528px;top:490px;width:186px;height:128px;transform:rotate(5deg)}
  .snap-jeeps div{background:linear-gradient(180deg,#b8c2cc 0%,#c89a6a 45%,#8a5a34 100%)}
  .snap-whale{left:458px;top:586px;width:186px;height:126px;transform:rotate(-4deg)}
  .snap-whale div{background:linear-gradient(180deg,#9aa8b6 0%,#4d6176 55%,#1e3148 100%)}
  .pin{position:absolute;width:12px;height:12px;border-radius:50%;background:var(--red)}
  .offer-seal{position:absolute;left:90px;top:622px;width:104px;height:104px;border-radius:50%;background:var(--red);transform:rotate(18deg);text-align:center;color:var(--white)}
  .offer-seal small{display:block;font-size:13px;font-weight:800;padding-top:26px;line-height:1}
  .offer-seal strong{display:block;font-size:28px;font-weight:900;color:var(--yellow);line-height:1}
  .offer-arrow{position:absolute;left:196px;top:640px}
  .customized{position:absolute;left:222px;top:650px;font-weight:800;font-size:33px;color:var(--red);line-height:1}
  .experience{position:absolute;left:224px;top:680px;font-family:"Kaushan Script",cursive;font-size:27px;color:#1e5fd0;line-height:1.1}
  .url-band{position:absolute;left:318px;top:793px;width:432px;height:35px;background:var(--url);color:var(--white);font-size:19px;letter-spacing:1.5px;line-height:35px;padding-left:22px}
  .url-band b{font-weight:800}
  .brand{position:absolute;left:62px;top:848px;font-weight:800;font-size:32px;color:var(--white);line-height:1}
  .partner{position:absolute;top:851px;background:#e9ecf2}
  .p1{left:354px;width:32px;height:38px;border-radius:3px}
  .p2{left:411px;width:38px;height:38px;border-radius:50%;background:#dfe8f5}
  .p3{left:471px;width:66px;height:26px;top:857px;border-radius:13px;opacity:.8}
  .p4{left:555px;width:66px;height:18px;top:861px;border-radius:3px;opacity:.8}
  .p5{left:635px;width:70px;height:18px;top:861px;border-radius:3px;opacity:.8}
</style>
</head>
<body>
<main class="booth-graphic">
  <div class="scene-top" role="img" aria-label="Photo of an icy blue glacier valley between mountains under green northern lights"></div>
  <div class="scene-bottom" role="img" aria-label="Photo of snowy mountains with a hiker carrying a backpack, fading to dark at the base"></div>
  <svg class="torn-panel" viewBox="0 0 750 260" preserveAspectRatio="none" aria-hidden="true">
    <defs>
      <linearGradient id="panelFade" x1="0" y1="0" x2="0" y2="1">
        <stop offset="0" stop-color="#fff"/><stop offset="0.78" stop-color="#fff"/><stop offset="1" stop-color="#fff" stop-opacity="0"/>
      </linearGradient>
    </defs>
    <path d="M0 12 L18 6 L34 10 L52 2 L70 8 L90 4 L110 9 L130 3 L150 7 L170 1 L192 8 L214 4 L236 10 L260 3 L284 9 L306 2 L330 8 L352 4 L376 10 L398 3 L420 8 L444 2 L468 7 L490 3 L514 9 L538 4 L560 10 L584 3 L606 8 L630 2 L652 9 L676 4 L700 10 L724 3 L750 8 L750 260 L0 260 Z" fill="url(#panelFade)"/>
  </svg>

  <div class="join">Join</div>
  <h1 class="headline">IRELANDS</h1>
  <div class="biggest-band"></div>
  <div class="biggest">BIGGEST</div>
  <div class="tours">Tours &amp; Travels</div>
  <div class="exhibition">EXHIBITION</div>

  <section class="info-box">
    <div class="booth-no"><small>BOOTH NO</small><strong>152</strong></div>
    <p class="info-text">Plan your ultimate Iceland vacation! Roam Kestal is a local Iceland Travel Agency dedicated to offering unforgettable day &amp; multi-day tours.</p>
  </section>

  <div class="tag tall tag-caves">CAVES &amp;<br>HORSEBACK<br>RIDING</div>
  <div class="tag tag-atv">ATV TOUR</div>
  <div class="tag tag-boat">BOAT TRIP</div>
  <div class="tag tag-sightseeing">SIGHTSEEING</div>
  <div class="tag tag-glacier">GLACIER WALKS</div>
  <div class="tag tag-whale">WHALE WATCHING</div>
  <div class="tag tag-buggy">BUGGY TOUR</div>
  <div class="tag tag-jeep">JEEP TOURS</div>

  <figure class="snapshot snap-cave"><div role="img" aria-label="Photo of a climber in a red jacket entering a rocky cave"></div></figure>
  <figure class="snapshot snap-jeeps"><div role="img" aria-label="Photo of off-road jeeps on a dirt track"></div></figure>
  <figure class="snapshot snap-whale"><div role="img" aria-label="Photo of a humpback whale breaching the sea"></div></figure>
  <span class="pin" style="left:594px;top:376px"></span>
  <span class="pin" style="left:660px;top:492px"></span>
  <span class="pin" style="left:560px;top:580px"></span>

  <div class="offer-seal"><small>WE ALSO</small><strong>OFFER</strong></div>
  <svg class="offer-arrow" width="60" height="30" viewBox="0 0 60 30" aria-hidden="true">
    <path d="M2 14 C14 2 30 2 40 10 C46 15 48 20 50 24" fill="none" stroke="#e5d400" stroke-width="2.5" stroke-linecap="round"/>
    <path d="M44 20 L50 26 L54 18" fill="none" stroke="#e5d400" stroke-width="2.5" stroke-linecap="round" stroke-linejoin="round"/>
  </svg>
  <div class="customized">CUSTOMIZED</div>
  <div class="experience">Travel experience</div>

  <div class="url-band">www.<b>brightfjordtrips</b>.example</div>
  <div class="brand">Roam Kestal</div>
  <span class="partner p1"></span>
  <span class="partner p2"></span>
  <span class="partner p3"></span>
  <span class="partner p4"></span>
  <span class="partner p5"></span>
</main>
</body>
</html>
```